Business card for massage therapy company called Blue Fern Wellness

Need business card for massage therapy company called Blue Fern Wellness. Would like my logo on the front and the back of the card I have 3 options of logos and you can play with what looks better.

Would like this information displayed on the back of the card:

Marcus Ellery
Licensed Massage Therapist
415-903-2264
bluefern-wellness.example
bluefern_wellness_

```html
<!DOCTYPE html>
<html lang="en">
<head>
<meta charset="utf-8">
<title>Blue Fern Wellness – Business Card</title>
<link rel="stylesheet" href="https://fonts.googleapis.com/css2?family=Montserrat:wght@400;500&family=Arimo:wght@400&display=swap">
<style>
  :root {
    --backdrop: #5b5b5b;
    --paper: #ffffff;
    --charcoal: #2e2e2e;
    --olive: #6f7459;
    --tan: #c79b79;
    --ink: #3d3d3d;
  }
  html, body {
    margin: 0;
    padding: 0;
    width: 1200px;
    height: 1200px;
    overflow: hidden;
    background: var(--backdrop);
  }
  .canvas {
    position: relative;
    width: 1200px;
    height: 1200px;
  }
  .card {
    position: absolute;
    left: 262px;
    width: 690px;
    height: 394px;
  }
  .card--front { top: 158px; background: var(--paper); }
  .card--back  { top: 651px; background: var(--charcoal); }

  .brand-name {
    position: absolute;
    left: 35px;
    top: 58px;
    margin: 0;
    font-family: "Montserrat", sans-serif;
    font-weight: 500;
    font-size: 27px;
    color: var(--olive);
    letter-spacing: 0.5px;
  }
  .person-name {
    position: absolute;
    left: 35px;
    top: 178px;
    margin: 0;
    font-family: "Montserrat", sans-serif;
    font-weight: 500;
    font-size: 25px;
    color: var(--olive);
    letter-spacing: 0.3px;
  }
  .person-title {
    position: absolute;
    left: 35px;
    top: 210px;
    margin: 0;
    font-family: "Arimo", sans-serif;
    font-size: 15px;
    color: var(--tan);
  }
  .address {
    position: absolute;
    left: 37px;
    top: 242px;
    margin: 0;
    font-family: "Arimo", sans-serif;
    font-style: normal;
    font-size: 16px;
    line-height: 21px;
    color: var(--ink);
  }
  .contact-list {
    position: absolute;
    left: 37px;
    top: 295px;
    margin: 0;
    padding: 0;
    list-style: none;
    font-family: "Arimo", sans-serif;
    font-size: 16px;
    color: var(--ink);
  }
  .contact-list li {
    display: flex;
    align-items: center;
    height: 20.5px;
  }
  .contact-icon {
    width: 14px;
    height: 14px;
    margin-right: 12px;
    fill: var(--olive);
  }
  .front-ring {
    position: absolute;
    left: 308px;
    top: 38px;
    width: 322px;
    height: 322px;
  }

  .back-lockup {
    position: absolute;
    left: 0;
    top: 80px;
    width: 100%;
    text-align: center;
  }
  .back-ring {
    display: block;
    margin: 0 auto;
    width: 136px;
    height: 136px;
  }
  .back-name {
    margin: 12px 0 0;
    font-family: "Montserrat", sans-serif;
    font-weight: 400;
    font-size: 40px;
    letter-spacing: 3px;
    line-height: 44px;
    color: var(--olive);
    text-transform: uppercase;
  }
  .back-name .line-sub {
    display: block;
    font-size: 21px;
    letter-spacing: 7px;
    line-height: 32px;
  }
</style>
</head>
<body>
<main class="canvas">

  <section class="card card--front" aria-label="Card front">
    <p class="brand-name">Blue Fern Wellness</p>
    <h1 class="person-name">MARCUS ELLERY</h1>
    <p class="person-title">Licensed Massage Therapist</p>
    <address class="address">2150 Juniper Row<br>Halden, Canada 41208</address>
    <ul class="contact-list">
      <li>
        <svg class="contact-icon" viewBox="0 0 24 24" aria-hidden="true"><path d="M6.6 10.8a15.2 15.2 0 0 0 6.6 6.6l2.2-2.2a1 1 0 0 1 1-.25 11.4 11.4 0 0 0 3.6.57 1 1 0 0 1 1 1V20a1 1 0 0 1-1 1A17 17 0 0 1 3 4a1 1 0 0 1 1-1h3.5a1 1 0 0 1 1 1c0 1.25.2 2.45.57 3.6a1 1 0 0 1-.25 1z"/></svg>
        415-903-2264
      </li>
      <li>
        <svg class="contact-icon" viewBox="0 0 24 24" aria-hidden="true"><path d="M2 6h20v12H2z M2 6l10 7 10-7" fill="var(--olive)"/><path d="M3 7l9 6 9-6" fill="none" stroke="#fff" stroke-width="1.6"/></svg>
        info@bluefern-wellness.example
      </li>
      <li>
        <svg class="contact-icon" viewBox="0 0 24 24" aria-hidden="true"><circle cx="12" cy="12" r="10"/><path d="M7 8c2 0 3 1 3 3s2 2 2 4-1 3-1 5M15 4c-1 2 0 3 2 3s3 2 3 3" fill="none" stroke="#fff" stroke-width="1.5"/></svg>
        www.bluefern-wellness.example
      </li>
    </ul>
    <svg class="front-ring" viewBox="0 0 322 322" aria-hidden="true">
      <circle cx="161" cy="161" r="157" fill="none" stroke="var(--olive)" stroke-width="2.6"/>
    </svg>
  </section>

  <section class="card card--back" aria-label="Card back">
    <div class="back-lockup">
      <svg class="back-ring" viewBox="0 0 136 136" aria-hidden="true">
        <circle cx="68" cy="68" r="66" fill="none" stroke="var(--olive)" stroke-width="1.6"/>
      </svg>
      <p class="back-name">Blue Fern<span class="line-sub">Wellness</span></p>
    </div>
  </section>

</main>
</body>
</html>
```